Online-Marketing Material für Recruiting-Plattform
Zielgruppe
Recruiting-Plattform für Physiotherapeuten. Wir sind Vermittler.
Aufgabenstellung
Ich benötige ein 2er Set aus Social-Media-Templates, das wir als Basis für Recruiting-Ads nutzen können.
Variante 1: (1080 x 1350) mit jeweils 285 Pixel Safe Space oben und unten (hier keine wichtigen Elemente).
Wichtig: Es handelt sich um ein Template. Daher muss es mit verschiedenen Elementen und Fotos funktionieren.
Die Elemente werden später durch variable Inhalte gesetzt. Ziel ist es, ein möglichst flexibles Format zu schaffen,
das mit unterschiedlichen Inhalten funktioniert.
Bitte orientiere dich am Grunddesign der Website therapunkt.de
Elemente und zugehörige Beispiele sind
1. Foto in querformat | Beispiel als Download)
2. Jobtitel als Headline | (Physiotherapeut (m/w/d)
3. Subtitle | Werde Teil eines wachsenden Teams
4. Arbeitszeitmodell | Vollzeit, Teilzeit
3. Ort | Hannover
4. 3 x Highlights | 1. Betriebliche Krankenversicherung 2. Tretlux 3. Gehalt bis zu 4.500 EUR
(Die Highlight variieren thematisch, daher hier bitte nur mit thematisch-neutralen Icons arbeiten.
5. Logo des Arbeitgebers (lusen) auf weiß
Variante 2 mit Foto in hochformat

```html
<!DOCTYPE html>
<html lang="de">
<head>
<meta charset="utf-8">
<title>lusen – Recruiting Templates</title>
<link rel="stylesheet" href="https://fonts.googleapis.com/css2?family=Montserrat:wght@600;700;800&display=swap">
<style>
  :root {
    --stage: #5e5e5e;
    --white: #ffffff;
    --teal: #0e97a0;
    --navy: #053a48;
    --yellow: #fbc63b;
    --divider: #c8c8c8;
    /* 285 px of 1350 px, scaled to the 662 px template height */
    --safe-zone: 140px;
  }
  * { box-sizing: border-box; margin: 0; padding: 0; }
  html, body { width: 1200px; height: 1117px; overflow: hidden; }
  body { background: var(--stage); font-family: "Montserrat", sans-serif; position: relative; }

  .template {
    position: absolute; top: 228px; width: 530px; height: 662px;
    background: var(--white); overflow: hidden;
    box-shadow: 0 6px 14px rgba(0,0,0,.35);
  }
  .template--landscape { left: 62px; }
  .template--portrait { left: 608px; }

  .template__blob { position: absolute; left: 0; top: 0; }

  .brand {
    position: absolute; top: 48px; left: 0; width: 100%;
    display: flex; justify-content: center; align-items: center; gap: 10px;
  }
  .brand__name { font-size: 46px; font-weight: 600; color: var(--navy); letter-spacing: 1px; line-height: 1; }
  .brand__dot { width: 22px; height: 22px; border-radius: 50%; background: var(--teal); }

  .job-title {
    position: absolute; top: 118px; width: 100%; text-align: center;
    font-size: 33px; font-weight: 800; color: var(--teal); letter-spacing: -0.4px; line-height: 1.2;
  }
  .job-subtitle {
    position: absolute; top: 164px; width: 100%; text-align: center;
    font-size: 18px; font-weight: 700; color: var(--navy); letter-spacing: -0.2px; line-height: 1.2;
  }

  .accent-bar {
    position: absolute; left: 0; width: 100%; height: 11px;
    background: linear-gradient(90deg, var(--teal) 0%, var(--teal) 25%, var(--yellow) 80%, var(--yellow) 100%);
  }
  .accent-bar--top { top: 196px; }
  .accent-bar--bottom { top: 651px; }

  .photo { position: absolute; top: 207px; left: 0; width: 100%; height: 260px; }
  .photo--landscape {
    background: linear-gradient(100deg, #e6dcc4 0%, #f6efdc 40%, #eee6d6 60%, #7b7a7d 85%, #5c5b5f 100%);
  }
  .photo--portrait {
    background:
      linear-gradient(180deg, rgba(255,255,255,0) 55%, rgba(220,220,218,.7) 100%),
      linear-gradient(90deg, #cfd8d3 0%, #eef0ef 25%, #f3f3f2 45%, #5f6f8c 58%, #e4e4e2 72%, #f2f2f1 100%);
  }

  .facts {
    position: absolute; top: 467px; left: 0; width: 100%; height: 37px;
    background: var(--navy); color: var(--white);
    display: flex; justify-content: center; align-items: center; gap: 24px;
    font-size: 18px; font-weight: 700;
  }
  .facts__item { display: flex; align-items: center; gap: 10px; }

  .highlights { position: absolute; top: 516px; left: 0; width: 100%; height: 130px; }
  .highlight { position: absolute; top: 0; width: 176px; margin-left: -88px; text-align: center; }
  .highlight--1 { left: 117px; }
  .highlight--2 { left: 265px; }
  .highlight--3 { left: 427px; }
  .highlight__icon {
    width: 65px; height: 65px; margin: 0 auto; border-radius: 50%;
    background: var(--teal); border: 4px solid var(--yellow);
    display: flex; align-items: center; justify-content: center;
  }
  .highlight__label {
    height: 52px; display: flex; align-items: center; justify-content: center;
    font-size: 14px; font-weight: 700; color: var(--navy); line-height: 1.2; margin-top: 4px;
  }
  .highlights__divider { position: absolute; top: 16px; width: 2px; height: 46px; background: var(--divider); }
  .highlights__divider--a { left: 192px; }
  .highlights__divider--b { left: 347px; }

  .template__wave { position: absolute; left: 0; top: 0; }
</style>
</head>
<body>

<!-- Variant 1: landscape photo -->
<article class="template template--landscape">
  <svg class="template__blob" width="100" height="190" viewBox="0 0 100 190" aria-hidden="true">
    <path fill="var(--yellow)" d="M0 183 L0 120 C10 100 20 90 20 60 C18 30 35 5 62 4 C84 4 92 30 84 50 C76 70 50 76 38 96 C28 116 36 140 30 160 C26 172 14 180 0 183 Z"/>
  </svg>
  <div class="brand"><span class="brand__name">lusen</span><span class="brand__dot"></span></div>
  <h1 class="job-title">Physiotherapeut (m/w/d)</h1>
  <p class="job-subtitle">Werde Teil eines wachsenden Teams</p>
  <div class="accent-bar accent-bar--top"></div>
  <div class="photo photo--landscape" role="img" aria-label="Querformat-Foto: heller Behandlungsraum mit Therapieliege, Sideboard und Wirbelsäulenmodell"></div>
  <div class="facts">
    <span class="facts__item">
      <svg width="20" height="20" viewBox="0 0 20 20" aria-hidden="true"><circle cx="10" cy="10" r="8.5" fill="none" stroke="#fff" stroke-width="1.6"/><path d="M10 5v5l3 2" fill="none" stroke="#fff" stroke-width="1.6" stroke-linecap="round"/></svg>
      Vollzeit | Teilzeit
    </span>
    <span class="facts__item">
      <svg width="16" height="20" viewBox="0 0 16 20" aria-hidden="true"><path d="M8 19s-6.5-6.5-6.5-11A6.5 6.5 0 0 1 14.5 8C14.5 12.5 8 19 8 19z" fill="none" stroke="#fff" stroke-width="1.6"/><circle cx="8" cy="8" r="2.4" fill="none" stroke="#fff" stroke-width="1.6"/></svg>
      Standort bei Hannover
    </span>
  </div>
  <div class="highlights">
    <div class="highlight highlight--1">
      <div class="highlight__icon"><svg width="36" height="24" viewBox="0 0 36 24" aria-hidden="true"><g fill="none" stroke="#fff" stroke-width="2" stroke-linecap="round" stroke-linejoin="round"><circle cx="8" cy="16" r="6"/><circle cx="28" cy="16" r="6"/><path d="M8 16l6-10h10l4 10M14 6l4 10h6M12 3h5M22 3h4"/></g></svg></div>
      <p class="highlight__label">Tretlux</p>
    </div>
    <span class="highlights__divider highlights__divider--a"></span>
    <div class="highlight highlight--2">
      <div class="highlight__icon"><svg width="30" height="32" viewBox="0 0 30 32" aria-hidden="true"><g fill="none" stroke="#fff" stroke-width="1.8" stroke-linejoin="round"><path d="M4 2h13l5 5v8M4 2v26h12"/><path d="M11 8v8M7 12h8M8 20h8M8 24h6"/><path d="M23 17l5 2v5c0 3-2.5 5-5 6-2.5-1-5-3-5-6v-5z"/></g></svg></div>
      <p class="highlight__label">Betriebliche<br>Krankenversicherung</p>
    </div>
    <span class="highlights__divider highlights__divider--b"></span>
    <div class="highlight highlight--3">
      <div class="highlight__icon"><svg width="34" height="28" viewBox="0 0 34 28" aria-hidden="true"><g fill="none" stroke="#fff" stroke-width="1.8" stroke-linejoin="round"><path d="M3 9l14-7 14 7-14 7z"/><path d="M3 13l14 7 14-7M3 17l14 7 14-7"/><ellipse cx="17" cy="9" rx="3.5" ry="2"/></g></svg></div>
      <p class="highlight__label">Gehalt bis zu<br>4.500 EUR</p>
    </div>
  </div>
  <div class="accent-bar accent-bar--bottom"></div>
  <svg class="template__wave" width="530" height="662" viewBox="0 0 530 662" aria-hidden="true">
    <path fill="var(--navy)" d="M346 662 C350 640 370 625 400 626 C430 628 440 658 470 657 C495 656 510 632 530 630 L530 662 Z"/>
  </svg>
</article>

<!-- Variant 2: portrait photo, cropped into the image field -->
<article class="template template--portrait">
  <svg class="template__blob" width="100" height="190" viewBox="0 0 100 190" aria-hidden="true">
    <path fill="var(--yellow)" d="M0 183 L0 120 C10 100 20 90 20 60 C18 30 35 5 62 4 C84 4 92 30 84 50 C76 70 50 76 38 96 C28 116 36 140 30 160 C26 172 14 180 0 183 Z"/>
  </svg>
  <div class="brand"><span class="brand__name">lusen</span><span class="brand__dot"></span></div>
  <h1 class="job-title">Physiotherapeut (m/w/d)</h1>
  <p class="job-subtitle">Werde Teil eines wachsenden Teams</p>
  <div class="accent-bar accent-bar--top"></div>
  <div class="photo photo--portrait" role="img" aria-label="Hochformat-Foto, in das Bildfeld zugeschnitten: Physiotherapeutin behandelt das Bein eines liegenden Patienten"></div>
  <div class="facts">
    <span class="facts__item">
      <svg width="20" height="20" viewBox="0 0 20 20" aria-hidden="true"><circle cx="10" cy="10" r="8.5" fill="none" stroke="#fff" stroke-width="1.6"/><path d="M10 5v5l3 2" fill="none" stroke="#fff" stroke-width="1.6" stroke-linecap="round"/></svg>
      Vollzeit | Teilzeit
    </span>
    <span class="facts__item">
      <svg width="16" height="20" viewBox="0 0 16 20" aria-hidden="true"><path d="M8 19s-6.5-6.5-6.5-11A6.5 6.5 0 0 1 14.5 8C14.5 12.5 8 19 8 19z" fill="none" stroke="#fff" stroke-width="1.6"/><circle cx="8" cy="8" r="2.4" fill="none" stroke="#fff" stroke-width="1.6"/></svg>
      Standort bei Hannover
    </span>
  </div>
  <div class="highlights">
    <div class="highlight highlight--1">
      <div class="highlight__icon"><svg width="36" height="24" viewBox="0 0 36 24" aria-hidden="true"><g fill="none" stroke="#fff" stroke-width="2" stroke-linecap="round" stroke-linejoin="round"><circle cx="8" cy="16" r="6"/><circle cx="28" cy="16" r="6"/><path d="M8 16l6-10h10l4 10M14 6l4 10h6M12 3h5M22 3h4"/></g></svg></div>
      <p class="highlight__label">Tretlux</p>
    </div>
    <span class="highlights__divider highlights__divider--a"></span>
    <div class="highlight highlight--2">
      <div class="highlight__icon"><svg width="30" height="32" viewBox="0 0 30 32" aria-hidden="true"><g fill="none" stroke="#fff" stroke-width="1.8" stroke-linejoin="round"><path d="M4 2h13l5 5v8M4 2v26h12"/><path d="M11 8v8M7 12h8M8 20h8M8 24h6"/><path d="M23 17l5 2v5c0 3-2.5 5-5 6-2.5-1-5-3-5-6v-5z"/></g></svg></div>
      <p class="highlight__label">Betriebliche<br>Krankenversicherung</p>
    </div>
    <span class="highlights__divider highlights__divider--b"></span>
    <div class="highlight highlight--3">
      <div class="highlight__icon"><svg width="34" height="28" viewBox="0 0 34 28" aria-hidden="true"><g fill="none" stroke="#fff" stroke-width="1.8" stroke-linejoin="round"><path d="M3 9l14-7 14 7-14 7z"/><path d="M3 13l14 7 14-7M3 17l14 7 14-7"/><ellipse cx="17" cy="9" rx="3.5" ry="2"/></g></svg></div>
      <p class="highlight__label">Gehalt bis zu<br>4.500 EUR</p>
    </div>
  </div>
  <div class="accent-bar accent-bar--bottom"></div>
  <svg class="template__wave" width="530" height="662" viewBox="0 0 530 662" aria-hidden="true">
    <path fill="var(--navy)" d="M346 662 C350 640 370 625 400 626 C430 628 440 658 470 657 C495 656 510 632 530 630 L530 662 Z"/>
  </svg>
</article>

</body>
</html>
```